Eye Doctor Needs Updated Business Card

We need a standard US business card designed for an optometrist's practice. Our practice name is Halvorn Vision Center and attached you'll find our logos. We are located in a smaller community, we are a trusted source for eye care and designer eyewear. We have 2 different version of our logos, so both versions are attached. Our slogan is "Small Town Values, World Class Care". I'd like to see designs with one of our logos on the front with our contact info, and have the slogan on the back by itself. Final design should be professional looking, include the colors of our logo or colors that compliment the logo. We want it to look appropriate for a healthcare practice but also up-to-date, eye-catching, to have the normal contact info like address, phone #, email, but also possibly room for additional contact info such as facebook.
Updates

I just uploaded .eps files to use instead of the jpeg. Hope that helps!

So many great designs! We tending to like the darker blues that are used in our logo as the main blue color for the business cards. We also really like the use of a water-mark type appearance on either the front and/or back, or the embossed look as well looks nice. Thank you all for such great designs!

We're preferring the designs where white and the darker blue used in our logo are the primary colors on the front, but with a little green used as well. Again though, thanks for all the impressive designs so far!

Industry/Entity Type

Healthcare

```html
<!DOCTYPE html>
<html lang="en">
<head>
<meta charset="utf-8">
<title>Halvorn Vision Center – Business Card</title>
<link href="https://fonts.googleapis.com/css2?family=Mulish:wght@400;600;700&display=swap" rel="stylesheet">
<style>
  :root {
    --stage: #d9dadb;
    --card: #ffffff;
    --card-shade: #eef0f1;
    --navy: #1d5a7c;
    --band: #1f6488;
    --green: #4a9a2a;
    --ink: #3d3f42;
    --muted: #6c6f73;
    --rule: #d3d6d9;
  }
  * { box-sizing: border-box; margin: 0; padding: 0; }
  html, body {
    width: 1200px; height: 871px; overflow: hidden;
    background: var(--stage);
    font-family: "Mulish", sans-serif;
  }
  .stage {
    position: relative; width: 1200px; height: 871px;
    display: flex; flex-direction: column; align-items: center;
    justify-content: center; gap: 44px;
  }
  .card {
    position: relative; width: 640px; height: 366px;
    background: linear-gradient(135deg, var(--card) 55%, var(--card-shade));
    box-shadow: 0 10px 28px rgba(0,0,0,.22);
    overflow: hidden;
  }
  .brand {
    display: flex; flex-direction: column; align-items: center; gap: 18px;
  }
  .brand-dot {
    width: 86px; height: 86px; border-radius: 50%;
    background: var(--navy);
  }
  .brand-name {
    font-weight: 700; color: var(--navy);
    font-size: 30px; letter-spacing: .5px; text-align: center; line-height: 1.1;
  }
  .slogan {
    font-size: 14px; font-weight: 600; color: var(--green);
    letter-spacing: 1.5px; text-transform: uppercase; text-align: center;
  }
  .card--back { display: flex; align-items: center; justify-content: center; }
  .card--front .brand-area {
    position: absolute; left: 0; top: 0; width: 300px; height: 296px;
    display: flex; align-items: center; justify-content: center;
  }
  .card--front .brand { gap: 16px; }
  .card--front .brand-dot { width: 74px; height: 74px; }
  .card--front .brand-name { font-size: 23px; max-width: 240px; }
  .divider {
    position: absolute; left: 312px; top: 30px; width: 1px; height: 236px;
    background: linear-gradient(var(--card), var(--rule) 30%, var(--rule) 70%, var(--card));
  }
  .contact {
    position: absolute; left: 345px; top: 42px; width: 280px; color: var(--muted);
  }
  .contact-name { font-weight: 700; font-size: 19px; color: var(--ink); }
  .contact-title { font-size: 13px; color: var(--green); margin-top: 5px; }
  .contact-address { font-size: 13px; line-height: 1.45; margin-top: 26px; }
  .contact-list { list-style: none; margin-top: 10px; font-size: 13px; }
  .contact-list li { display: flex; align-items: center; gap: 12px; height: 22px; }
  .contact-list svg { width: 13px; height: 13px; flex: none; }
  .band {
    position: absolute; left: 0; bottom: 0; width: 100%; height: 70px;
    background: var(--band);
    display: flex; align-items: center; justify-content: center; gap: 14px;
    color: #e8f0f5; font-size: 16px; letter-spacing: .5px;
  }
  .band-mark { width: 14px; height: 14px; border-radius: 50%; border: 1.5px solid #e8f0f5; }
</style>
</head>
<body>
<main class="stage">
  <section class="card card--back" aria-label="Card back">
    <div class="brand">
      <span class="brand-dot"></span>
      <span class="brand-name">Halvorn Vision Center</span>
      <span class="slogan">Small Town Values, World Class Care</span>
    </div>
  </section>

  <section class="card card--front" aria-label="Card front">
    <div class="brand-area">
      <div class="brand">
        <span class="brand-dot"></span>
        <span class="brand-name">Halvorn Vision Center</span>
      </div>
    </div>
    <span class="divider"></span>
    <div class="contact">
      <p class="contact-name">Marlo Fenwick</p>
      <p class="contact-title">Owner/Optometrist</p>
      <p class="contact-address">4417 W. Orchard Ln. Ste. 210<br>Brenton, Az. 85990</p>
      <ul class="contact-list">
        <li>
          <svg viewBox="0 0 16 16" fill="var(--green)"><path d="M3 1.5l3 .5 1 3.2-1.8 1.3a9 9 0 0 0 4.3 4.3L10.8 9l3.2 1 .5 3-2 1.5C6.5 14 2 9.5 1.5 3.5z"/></svg>
          555.014.2290
        </li>
        <li>
          <svg viewBox="0 0 16 16" fill="none" stroke="var(--green)" stroke-width="1.6"><rect x="1.5" y="3.5" width="13" height="9"/><path d="M1.5 3.5L8 9l6.5-5.5"/></svg>
          hello@halvornvision.example
        </li>
        <li>
          <svg viewBox="0 0 16 16" fill="none" stroke="var(--green)" stroke-width="1.5"><circle cx="8" cy="8" r="6.5"/><path d="M1.5 8h13M8 1.5c-3 3.5-3 9.5 0 13M8 1.5c3 3.5 3 9.5 0 13"/></svg>
          www.halvornvision.example
        </li>
      </ul>
    </div>
    <div class="band">
      <span class="band-mark"></span>
      <span>www.halvornvision.example</span>
    </div>
  </section>
</main>
</body>
</html>
```